Country Duo act needs single artwork

We need artwork for our latest single for quavera and other music streaming sites. The design can include the pictures in the attached files that we uploaded but we are also open to designs that also don't include them. It should be easy to read the song title
"Rain Keeps Turning" and our band name Harbor 82 - this track is our actual story. Must be at least 640 x 640 pixels to be acceptable to quavera. We have also included a copy of the track for inspiration.
Check us out on quavera to see other artwork -> https://open.quavera-tunes.example/artist/4kTqZbN7rW2mLxPd9HsVyE?si=Hc8Jw2TnQpLm5VaRkXbYzG

Target Market(s)

Country music fans

Industry/Entity Type

Music

Font styles to use
Decorative

Colors

Designer to choose colors to be used in the design.

Requirements
Must have
• Name of song Title and band name
Nice to have
• Vibe that matches the song / one of our pictures included
Should not have
• any other text

```html
<!DOCTYPE html>
<html lang="en">
<head>
<meta charset="utf-8">
<title>Rain Keeps Turning – Harbor 82</title>
<link rel="stylesheet" href="https://fonts.googleapis.com/css2?family=Bowlby+One&family=Montserrat:wght@700&display=swap">
<style>
  :root {
    --sky: #7bc4cc;
    --title-blue: #3b8bb0;
    --white: #ffffff;
  }
  html, body {
    margin: 0;
    padding: 0;
    overflow: hidden;
    background: var(--sky);
  }
  .single-cover {
    position: relative;
    width: 1197px;
    height: 1200px;
    background: var(--sky);
    overflow: hidden;
  }
  .cover-art {
    position: absolute;
    inset: 0;
    width: 1197px;
    height: 1200px;
  }
  .song-title text {
    font-family: "Bowlby One", "Arial Black", sans-serif;
    fill: var(--title-blue);
    text-anchor: middle;
    letter-spacing: 16px;
  }
  .reaching-arms rect {
    fill: var(--white);
  }
  .band-name {
    position: absolute;
    left: 0;
    right: 0;
    top: 1012px;
    margin: 0;
    text-align: center;
    font-family: "Montserrat", "Helvetica", sans-serif;
    font-weight: 700;
    font-size: 94px;
    letter-spacing: 6px;
    line-height: 1;
    color: var(--white);
  }
</style>
</head>
<body>
  <main class="single-cover">
    <svg class="cover-art" viewBox="0 0 1197 1200" xmlns="http://www.w3.org/2000/svg">
      <g class="song-title" aria-label="Rain Keeps Turning">
        <text x="600" y="420" font-size="390" textLength="900" lengthAdjust="spacingAndGlyphs">RAIN</text>
        <text x="600" y="590" font-size="192" textLength="900" lengthAdjust="spacingAndGlyphs">KEEPS</text>
        <text x="600" y="990" font-size="350" textLength="900" lengthAdjust="spacingAndGlyphs">TURNING</text>
      </g>
      <g class="reaching-arms" role="img" aria-label="Illustration of two white arms reaching toward each other between the title lines">
        <rect x="-20" y="618" width="540" height="78" rx="39"/>
        <rect x="680" y="612" width="537" height="80" rx="40"/>
      </g>
    </svg>
    <h2 class="band-name">HARBOR 82</h2>
  </main>
</body>
</html>
```